NEW Modern Sleek Business Card for VR Language Startup

Our startup is using VR to lead the next wave of world language education. We need a two-sided business card that introduces the larger organization (Quorvel Language Inc) and our contact info on one side and shows the product, Lumidrasca, on the other side.

Side 1 (contact info)= Quorvel Logo and Contact info (name, title, phone, email)

Side 2 (product)= Lumidrasc logo, text, and website
Text= Culturally Immersive Language Learning Games
Website= www.lumidrasc.example

Target Market(s)

Education, Technology

Contact Information for Business Card

Contact info will be updated upon approval of the design. For now, put this as a placeholder.

Perry Hollins
Founder & CEO
phollins@mailtrove.example
(555)-014-2736

Font styles to use
Other font styles liked:
• Gibson and Century Gothic are the brand fonts

Requirements
Nice to have
• I would love to see cohesion between the design and colors of the two logos. I have attached a few business card designs that I like, so you can get a feel for my preferred style.

```html
<!DOCTYPE html>
<html lang="en">
<head>
<meta charset="utf-8">
<title>Quorvel Language Inc – Business Card</title>
<link rel="stylesheet" href="https://fonts.googleapis.com/css2?family=Montserrat:wght@600;700&family=Questrial&display=swap">
<style>
  :root {
    --backdrop: #1d1e21;
    --card-white: #ffffff;
    --ink-grey: #5a5a5e;
    --accent-orange: #f47a26;
    --accent-red: #ee3a3a;
    --grad-cyan: #19e6ea;
    --grad-blue: #3f8cf0;
    --grad-violet: #7a3cf2;
    --band-white: #ffffff;
  }
  * { box-sizing: border-box; margin: 0; padding: 0; }
  html, body {
    width: 1200px; height: 1200px; overflow: hidden;
    background: var(--backdrop);
  }
  .sheet {
    width: 1200px; height: 1200px;
    display: flex; flex-direction: column; align-items: center; justify-content: center;
    gap: 60px;
  }
  .card {
    position: relative;
    width: 840px; height: 480px;
    border-radius: 34px;
    overflow: hidden;
  }

  /* Product side */
  .card--product {
    background: linear-gradient(135deg, var(--grad-cyan) 0%, var(--grad-blue) 50%, var(--grad-violet) 100%);
  }
  .product-mark {
    position: absolute; top: 120px; left: 0; right: 0;
    display: flex; align-items: center; justify-content: center; gap: 26px;
  }
  .mark-dot {
    width: 64px; height: 64px; border-radius: 50%;
    background: var(--card-white);
  }
  .mark-name {
    font-family: "Montserrat", sans-serif; font-weight: 700;
    font-size: 64px; letter-spacing: 8px; color: var(--card-white);
  }
  .website {
    position: absolute; left: 0; right: 0; top: 300px; text-align: center;
    font-family: "Montserrat", sans-serif; font-weight: 700;
    font-size: 24px; color: var(--card-white); letter-spacing: 1px;
  }
  .tagline-band {
    position: absolute; left: 0; right: 0; top: 356px; height: 56px;
    background: var(--band-white);
    display: flex; align-items: center; justify-content: center;
  }
  .tagline {
    font-family: "Montserrat", sans-serif; font-weight: 700;
    font-size: 27px; color: var(--accent-orange); letter-spacing: 0.5px;
  }

  /* Contact side */
  .card--contact { background: var(--card-white); }
  .edge-line {
    position: absolute; top: 0; bottom: 0; width: 2px;
    background: linear-gradient(180deg, var(--accent-orange), var(--accent-red));
  }
  .edge-line--left { left: 28px; }
  .edge-line--right { right: 28px; }
  .brand-lockup {
    position: absolute; left: 70px; top: 0; bottom: 0; width: 350px;
    display: flex; flex-direction: column; align-items: center; justify-content: center; gap: 26px;
  }
  .brand-dot {
    width: 130px; height: 130px; border-radius: 50%;
    background: linear-gradient(135deg, var(--grad-cyan), var(--grad-violet));
  }
  .brand-name {
    font-family: "Questrial", sans-serif; font-size: 58px; color: var(--ink-grey);
  }
  .divider {
    position: absolute; left: 440px; top: 195px; width: 2px; height: 90px;
    background: var(--accent-red);
  }
  .contact-block {
    position: absolute; left: 490px; top: 0; bottom: 0;
    display: flex; flex-direction: column; justify-content: center;
    font-family: "Questrial", sans-serif; color: var(--ink-grey);
  }
  .contact-name { font-size: 36px; }
  .contact-title {
    font-family: "Montserrat", sans-serif; font-weight: 600;
    font-size: 26px; color: var(--accent-orange); margin: 4px 0 14px;
  }
  .contact-line { font-size: 21px; line-height: 1.4; }
</style>
</head>
<body>
  <main class="sheet">
    <section class="card card--product" aria-label="Product side">
      <div class="product-mark">
        <span class="mark-dot"></span>
        <span class="mark-name">LUMIDRASC</span>
      </div>
      <p class="website">www.lumidrasc.example</p>
      <div class="tagline-band">
        <p class="tagline">Culturally Immersive Language Learning Games</p>
      </div>
    </section>

    <section class="card card--contact" aria-label="Contact side">
      <span class="edge-line edge-line--left"></span>
      <span class="edge-line edge-line--right"></span>
      <div class="brand-lockup">
        <span class="brand-dot"></span>
        <span class="brand-name">Quorvel</span>
      </div>
      <span class="divider"></span>
      <div class="contact-block">
        <p class="contact-name">Perry Hollins</p>
        <p class="contact-title">Founder &amp; CEO</p>
        <p class="contact-line">phollins@mailtrove.example</p>
        <p class="contact-line">(555)-014-2736</p>
      </div>
    </section>
  </main>
</body>
</html>
```